Doctor's Office Intake Forms

Hi,

I am looking to have the following form to be replicated and combined with the other files. I do not want this form merely digitized but a new form to be created but asking the same questions with our logo etc. Please add a section for allergies and medications taken. For the Sexually transmitted infections the choices are the ones listed plus Pelvic Inflammatory Disease, Syphilis, HIV, and Hepatitis.

Please use common sense. The example file provided is a print out of a digital intake form.

Medical

Sans Serif

• Good format

```html
<!DOCTYPE html>
<html lang="en">
<head>
<meta charset="utf-8">
<title>HWA Onboarding Forms</title>
<link href="https://fonts.googleapis.com/css2?family=Montserrat:ital,wght@0,400;0,500;0,600;0,700;0,800;1,500&display=swap" rel="stylesheet">
<style>
:root{
  --bg:#e7ecf8;
  --paper:#ffffff;
  --ink:#1d1d2b;
  --text:#3a3a48;
  --field:#f0f0f3;
  --field-edge:#e2e2e8;
  --rule:#ececf2;
  --brand:#e3398f;
  --pill:#25252f;
  --grad:linear-gradient(90deg,#ff7a2f 0%,#f0328c 35%,#7b3fe4 70%,#1e8bff 100%);
  --grad-line:linear-gradient(90deg,#f0328c 0%,#9b4de6 50%,#2a8cff 100%);
}
*{margin:0;padding:0;box-sizing:border-box}
html,body{width:1200px;height:720px;overflow:hidden}
body{background:var(--bg);font-family:'Montserrat',sans-serif;color:var(--text);position:relative}

.pg{position:absolute;width:216px;height:278px;background:var(--paper);box-shadow:0 1px 3px rgba(40,50,90,.12);overflow:hidden}
.pg::after{content:"";position:absolute;left:0;right:0;bottom:0;height:1.6px;background:var(--grad)}

.brand{position:absolute;display:flex;align-items:center;gap:1.6px;font-weight:800;color:var(--brand);letter-spacing:.2px}
.brand .dot{border-radius:50%;background:var(--brand)}
.brand.sm{left:12px;top:10px;font-size:7px}
.brand.sm .dot{width:6px;height:6px}
.brand.md{left:11px;top:12px;font-size:10.5px}
.brand.md .dot{width:8px;height:8px}
.brand.lg{left:0;right:0;top:14px;justify-content:center;font-size:12px}
.brand.lg .dot{width:10px;height:10px}

.pill{position:absolute;left:115px;top:13px;width:101px;height:9px;background:var(--pill);border-radius:5px 0 0 5px;color:#fff;font-size:5.4px;font-weight:600;letter-spacing:1.5px;display:flex;align-items:center;justify-content:center}

.sh{position:absolute;left:14px;right:14px;font-size:4.2px;font-weight:700;color:var(--ink);padding-bottom:1.5px}
.sh::after{content:"";position:absolute;left:0;right:0;bottom:0;height:.5px;background:var(--grad-line)}
.sh.plain{font-weight:600}

.f{position:absolute;left:14px;right:14px;display:flex;align-items:center;gap:1.5px;height:5.5px;font-size:3.1px;white-space:nowrap}
.f i{flex:1;height:5.5px;background:var(--field)}
.f .gap{margin-left:8px}
.lbl{position:absolute;font-size:3.1px;white-space:nowrap}
.lbl.b{font-weight:700;color:var(--ink)}
.area{position:absolute;left:14px;right:14px;background:var(--field)}
.cell{position:absolute;height:6px;background:var(--field)}

.opt{position:absolute;display:flex;align-items:center;gap:3px;font-size:3.1px;white-space:nowrap}
.cb{display:inline-block;width:5px;height:5px;background:var(--field);border:.3px solid var(--field-edge)}
.row-line{position:absolute;left:14px;right:14px;height:.3px;background:var(--rule)}

.title{position:absolute;left:18px;right:18px;top:43px;text-align:center;font-size:5.9px;font-weight:700;color:var(--ink);line-height:7.6px;padding-bottom:2px}
.title::after{content:"";position:absolute;left:4px;right:4px;bottom:0;height:.5px;background:var(--grad-line)}
.copy{position:absolute;left:24px;right:23px;font-size:3.3px;line-height:4.3px;text-align:justify;color:var(--text)}
.copy p{margin-bottom:4.5px}
.copy strong{color:var(--ink);font-weight:700}
.copy ul{list-style:none;padding-left:13px;margin-bottom:2px}
.copy ol{padding-left:7px;margin-bottom:4.5px}
.copy ol li{margin-bottom:4px;padding-left:2px}
.sig{position:absolute;top:254px;width:45px;border-top:.5px dashed #555;font-size:3.1px;text-align:center;padding-top:3px}
.req{position:absolute;left:152px;font-style:italic;font-weight:500;font-size:3.1px}
</style>
</head>
<body>

<section class="pg" style="left:40px;top:74px">
  <div class="brand md"><span class="dot"></span>HWA</div>
  <div class="pill">ONBOARDING FORMS</div>

  <h2 class="sh" style="top:39px">NAME &amp; GENDER</h2>
  <div class="f" style="top:51px"><span>First Name:</span><i></i></div>
  <div class="f" style="top:61px"><span>Middle Name:</span><i></i></div>
  <div class="f" style="top:71px"><span>Last Name:</span><i></i></div>
  <div class="f" style="top:81px"><span>Suffix:</span><i></i></div>
  <div class="f" style="top:90px"><span>Nickname:</span><i></i></div>
  <div class="f" style="top:100px"><span>Sex:</span><i></i></div>
  <div class="f" style="top:110px"><span>Gender Identity:</span><i></i></div>
  <div class="f" style="top:120px"><span>Sexual Orientation:</span><i></i></div>

  <h2 class="sh" style="top:138px">PATIENT BACKGROUND</h2>
  <div class="f" style="top:150px"><span>Date of Birth:</span><i style="flex:none;width:40px"></i><span class="gap">Preferred Language:</span><i></i></div>
  <div class="f" style="top:160px"><span>Social Security #:</span><i style="flex:none;width:42px"></i><span class="gap">Race:</span><i></i></div>
  <div class="f" style="top:170px"><span>Ethnicity:</span><i style="flex:none;width:53px"></i></div>

  <h2 class="sh" style="top:187px">CONTACT INFORMATION</h2>
  <div class="f" style="top:199px"><span>Email Address:</span><i></i></div>
  <div class="f" style="top:209px"><span>Home Phone:</span><i></i><span class="gap">Cell Phone:</span><i></i><span class="gap">Work Phone:</span><i></i></div>

  <h2 class="sh" style="top:223px">ADDRESS</h2>
  <span class="lbl" style="left:14px;top:235px">Street Address:</span>
  <div class="area" style="left:40px;top:234px;height:16px"></div>
  <div class="f" style="top:253px"><span>City:</span><i></i><span class="gap">State:</span><i></i><span class="gap">Zip Code:</span><i></i></div>
</section>

<section class="pg" style="left:266px;top:74px">
  <div class="brand sm"><span class="dot"></span>HWA</div>

  <h2 class="sh" style="top:29px">EMERGENCY CONTACT</h2>
  <div class="f" style="top:41px"><span>Name:</span><i></i></div>
  <div class="f" style="top:51px"><span>Relation:</span><i></i><span class="gap">Phone:</span><i style="flex:.6"></i></div>

  <h2 class="sh" style="top:65px">ADDITIONAL INFORMATION</h2>
  <div class="f" style="top:77px"><span>Preferred Pronouns:</span><i></i></div>
  <div class="f" style="top:87px"><span>Who referred you?:</span><i></i></div>
  <span class="opt" style="left:19px;top:97px"><b class="cb"></b>Do you use online scheduling?</span>
  <span class="opt" style="left:94px;top:97px"><b class="cb"></b>Want access to online portal?</span>
  <span class="lbl" style="left:14px;top:106px">Anything special we need to know:</span>
  <div class="area" style="top:111px;height:15px"></div>

  <h2 class="sh" style="top:135px">CHANGES TO MEDICATIONS</h2>
  <span class="lbl b" style="left:14px;top:145px">Medication &amp; Dosage</span>
  <span class="lbl b" style="left:141px;top:145px">Indication</span>
  <div class="cell" style="left:14px;width:124px;top:151px"></div><div class="cell" style="left:140px;width:62px;top:151px"></div>
  <div class="cell" style="left:14px;width:124px;top:158px"></div><div class="cell" style="left:140px;width:62px;top:158px"></div>
  <div class="cell" style="left:14px;width:124px;top:165px"></div><div class="cell" style="left:140px;width:62px;top:165px"></div>
  <span class="lbl" style="left:14px;top:175px">Changes to medications:</span>
  <div class="area" style="top:180px;height:15px"></div>

  <h2 class="sh" style="top:205px">CHANGES TO ALLERGIES</h2>
  <span class="lbl b" style="left:14px;top:215px">Allergy</span>
  <span class="lbl b" style="left:141px;top:215px">Reaction</span>
  <div class="cell" style="left:14px;width:124px;top:221px"></div><div class="cell" style="left:140px;width:62px;top:221px"></div>
  <div class="cell" style="left:14px;width:124px;top:228px"></div><div class="cell" style="left:140px;width:62px;top:228px"></div>
  <div class="cell" style="left:14px;width:124px;top:235px"></div><div class="cell" style="left:140px;width:62px;top:235px"></div>
  <span class="lbl" style="left:14px;top:245px">Changes to allergies:</span>
  <div class="area" style="top:250px;height:15px"></div>
</section>

<section class="pg" style="left:492px;top:74px">
  <div class="brand sm"><span class="dot"></span>HWA</div>

  <h2 class="sh" style="top:29px">CHANGES TO MEDICAL CONDITIONS</h2>
  <span class="lbl b" style="left:14px;top:40px">Problem</span>
  <span class="lbl b" style="left:65px;top:40px">Code</span>
  <span class="lbl b" style="left:103px;top:40px">Status</span>
  <span class="lbl b" style="left:153px;top:40px">Diagnosed</span>
  <div class="cell" style="left:14px;width:48px;top:45px"></div><div class="cell" style="left:63px;width:38px;top:45px"></div><div class="cell" style="left:102px;width:50px;top:45px"></div><div class="cell" style="left:153px;width:49px;top:45px"></div>
  <div class="cell" style="left:14px;width:48px;top:52px"></div><div class="cell" style="left:63px;width:38px;top:52px"></div><div class="cell" style="left:102px;width:50px;top:52px"></div><div class="cell" style="left:153px;width:49px;top:52px"></div>
  <div class="cell" style="left:14px;width:48px;top:59px"></div><div class="cell" style="left:63px;width:38px;top:59px"></div><div class="cell" style="left:102px;width:50px;top:59px"></div><div class="cell" style="left:153px;width:49px;top:59px"></div>
  <div class="cell" style="left:14px;width:48px;top:66px"></div><div class="cell" style="left:63px;width:38px;top:66px"></div><div class="cell" style="left:102px;width:50px;top:66px"></div><div class="cell" style="left:153px;width:49px;top:66px"></div>
  <span class="lbl" style="left:14px;top:79px">Changes to medical conditions:</span>
  <div class="area" style="top:84px;height:15px"></div>

  <h2 class="sh" style="top:109px">PRIMARY INSURANCE</h2>
  <div class="f" style="top:121px"><span>Primary Insurance Company:</span><i></i></div>
  <div class="f" style="top:131px"><span>Plan Name:</span><i></i></div>
  <div class="f" style="top:141px"><span>Insurance ID Number:</span><i></i><span class="gap">Group Number:</span><i style="flex:.8"></i></div>
  <div class="f" style="top:151px"><span>Patient Student Status:</span><i></i></div>
  <span class="opt" style="left:18px;top:162px"><b class="cb"></b>Are you the insurance subscriber?</span>

  <h2 class="sh" style="top:178px">REASONS FOR VISIT</h2>
  <span class="lbl" style="left:14px;top:191px">Hepatitis C (Prevention, Testing, and Treatment)</span>
  <span class="opt" style="left:107px;top:190px"><b class="cb"></b>Yes</span><span class="opt" style="left:132px;top:190px"><b class="cb"></b>No</span>
  <span class="lbl" style="left:14px;top:201px">HIV (Prevention, Testing, and Treatment)</span>
  <span class="opt" style="left:107px;top:200px"><b class="cb"></b>Yes</span><span class="opt" style="left:132px;top:200px"><b class="cb"></b>No</span>
  <span class="lbl" style="left:14px;top:211px">Are You On PrEP?</span>
  <span class="opt" style="left:107px;top:210px"><b class="cb"></b>Yes</span><span class="opt" style="left:132px;top:210px"><b class="cb"></b>No</span>

  <h2 class="sh plain" style="top:222px">Personal Medical History</h2>
  <span class="lbl b" style="left:14px;top:232px">Have You Ever Been Diagnosed With;</span>
  <span class="lbl" style="left:21px;top:242px">Allergies:</span>
  <span class="opt" style="left:50px;top:241px"><b class="cb"></b>Yes</span><span class="opt" style="left:75px;top:241px"><b class="cb"></b>No</span>
  <div class="f" style="top:250px;left:21px"><span>What Are You Allergic To?</span><i></i></div>
  <span class="lbl" style="left:21px;top:263px">Anxiety:</span>
  <span class="opt" style="left:50px;top:262px"><b class="cb"></b>Yes</span><span class="opt" style="left:75px;top:262px"><b class="cb"></b>No</span>
</section>

<section class="pg" style="left:718px;top:74px">
  <div class="brand sm"><span class="dot"></span>HWA</div>

  <span class="lbl" style="left:21px;top:29px">Asthma:</span><span class="opt" style="left:89px;top:28px"><b class="cb"></b>Yes</span><span class="opt" style="left:115px;top:28px"><b class="cb"></b>No</span><div class="row-line" style="top:36px"></div>
  <span class="lbl" style="left:21px;top:42px">Cancer:</span><span class="opt" style="left:89px;top:41px"><b class="cb"></b>Yes</span><span class="opt" style="left:115px;top:41px"><b class="cb"></b>No</span><div class="row-line" style="top:48px"></div>
  <span class="lbl" style="left:21px;top:54px">Depression:</span><span class="opt" style="left:89px;top:53px"><b class="cb"></b>Yes</span><span class="opt" style="left:115px;top:53px"><b class="cb"></b>No</span><div class="row-line" style="top:61px"></div>
  <span class="lbl" style="left:21px;top:66px">Diabetes:</span><span class="opt" style="left:89px;top:65px"><b class="cb"></b>Yes</span><span class="opt" style="left:115px;top:65px"><b class="cb"></b>No</span><div class="row-line" style="top:73px"></div>
  <span class="lbl" style="left:21px;top:79px">Heart Disease:</span><span class="opt" style="left:89px;top:78px"><b class="cb"></b>Yes</span><span class="opt" style="left:115px;top:78px"><b class="cb"></b>No</span><div class="row-line" style="top:85px"></div>
  <span class="lbl" style="left:21px;top:91px">Hepatitis or Liver Dysfunction:</span><span class="opt" style="left:89px;top:90px"><b class="cb"></b>Yes</span><span class="opt" style="left:115px;top:90px"><b class="cb"></b>No</span><div class="row-line" style="top:98px"></div>
  <span class="lbl" style="left:21px;top:104px">High Blood Pressure:</span><span class="opt" style="left:89px;top:103px"><b class="cb"></b>Yes</span><span class="opt" style="left:115px;top:103px"><b class="cb"></b>No</span><div class="row-line" style="top:110px"></div>
  <span class="lbl" style="left:21px;top:116px">High Cholesterol:</span><span class="opt" style="left:89px;top:115px"><b class="cb"></b>Yes</span><span class="opt" style="left:115px;top:115px"><b class="cb"></b>No</span><div class="row-line" style="top:123px"></div>
  <span class="lbl" style="left:21px;top:128px">HIV/AIDS:</span><span class="opt" style="left:89px;top:127px"><b class="cb"></b>Yes</span><span class="opt" style="left:115px;top:127px"><b class="cb"></b>No</span><div class="row-line" style="top:135px"></div>
  <span class="lbl" style="left:21px;top:141px">Kidney Disease:</span><span class="opt" style="left:89px;top:140px"><b class="cb"></b>Yes</span><span class="opt" style="left:115px;top:140px"><b class="cb"></b>No</span><div class="row-line" style="top:147px"></div>
  <span class="lbl" style="left:21px;top:153px">Mental Health Condition:</span><span class="opt" style="left:89px;top:152px"><b class="cb"></b>Yes</span><span class="opt" style="left:115px;top:152px"><b class="cb"></b>No</span><div class="row-line" style="top:160px"></div>
  <span class="lbl" style="left:21px;top:166px">Neurological Conditions:</span><span class="opt" style="left:89px;top:165px"><b class="cb"></b>Yes</span><span class="opt" style="left:115px;top:165px"><b class="cb"></b>No</span><div class="row-line" style="top:172px"></div>

  <span class="lbl" style="left:21px;top:179px">Sexually Transmitted Infections:</span>
  <span class="opt" style="left:28px;top:187px"><b class="cb"></b>Chlamydia</span>
  <span class="opt" style="left:66px;top:187px"><b class="cb"></b>Gonorrhea</span>
  <span class="opt" style="left:105px;top:187px"><b class="cb"></b>Herpes</span>
  <span class="opt" style="left:130px;top:187px"><b class="cb"></b>Pelvic Inflammatory Disease</span>
  <span class="opt" style="left:28px;top:197px"><b class="cb"></b>HPV</span>
  <span class="opt" style="left:66px;top:197px"><b class="cb"></b>Syphilis</span>
  <span class="opt" style="left:105px;top:197px"><b class="cb"></b>HIV</span>
  <span class="opt" style="left:130px;top:197px"><b class="cb"></b>Hepatitis</span>
  <div class="row-line" style="top:206px"></div>
  <span class="lbl" style="left:21px;top:212px">TB:</span><span class="opt" style="left:89px;top:211px"><b class="cb"></b>Yes</span><span class="opt" style="left:115px;top:211px"><b class="cb"></b>No</span>
  <span class="lbl" style="left:14px;top:225px">Do You Take Any Medications or Supplements? If so, please list.</span>
  <div class="area" style="top:230px;height:16px"></div>
</section>

<section class="pg" style="left:943px;top:74px">
  <div class="brand sm"><span class="dot"></span>HWA</div>

  <h2 class="sh plain" style="top:27px">Social History</h2>
  <span class="lbl" style="left:21px;top:39px">Do You Use</span>
  <span class="opt" style="left:28px;top:47px"><b class="cb"></b>Alcohol</span>
  <span class="opt" style="left:66px;top:47px"><b class="cb"></b>Cigarettes</span>
  <span class="opt" style="left:105px;top:47px"><b class="cb"></b>Illicit Drugs</span>
  <span class="opt" style="left:143px;top:47px"><b class="cb"></b>Smoke</span>
  <div class="f" style="top:60px;left:21px"><span>How Many Sexual Partners Have You Had In The Last 30 Days?</span><i></i></div>
  <div class="f" style="top:72px;left:21px"><span>How Many Sexual Partners Have You Had In Your Lifetime?</span><i></i></div>
  <span class="lbl" style="left:21px;top:86px">Do You Use Condoms?</span><span class="opt" style="left:89px;top:85px"><b class="cb"></b>Yes</span><span class="opt" style="left:115px;top:85px"><b class="cb"></b>No</span><div class="row-line" style="top:93px"></div>
  <span class="lbl" style="left:21px;top:99px">Do You Engage In Anal Sex?</span><span class="opt" style="left:89px;top:98px"><b class="cb"></b>Give</span><span class="opt" style="left:115px;top:98px"><b class="cb"></b>Receive</span><span class="opt" style="left:153px;top:98px"><b class="cb"></b>No</span><div class="row-line" style="top:106px"></div>
  <span class="lbl" style="left:21px;top:112px">Do You Engage In Oral Sex?</span><span class="opt" style="left:89px;top:111px"><b class="cb"></b>Yes</span><span class="opt" style="left:115px;top:111px"><b class="cb"></b>No</span><div class="row-line" style="top:118px"></div>
  <span class="lbl" style="left:21px;top:124px">Do You Engage In Vaginal Sex?</span><span class="opt" style="left:89px;top:123px"><b class="cb"></b>Give</span><span class="opt" style="left:115px;top:123px"><b class="cb"></b>Receive</span><span class="opt" style="left:153px;top:123px"><b class="cb"></b>No</span><div class="row-line" style="top:131px"></div>
  <span class="lbl" style="left:21px;top:137px">Do You Consider Yourself A Sex Worker?</span><span class="opt" style="left:89px;top:136px"><b class="cb"></b>Yes</span><span class="opt" style="left:115px;top:136px"><b class="cb"></b>No</span><div class="row-line" style="top:143px"></div>
  <span class="lbl" style="left:21px;top:149px">Is There A Chance You May Be Pregnant?</span><span class="opt" style="left:89px;top:148px"><b class="cb"></b>Yes</span><span class="opt" style="left:115px;top:148px"><b class="cb"></b>No</span>

  <h2 class="sh" style="top:168px">QUESTIONS &amp; COMMENTS</h2>
  <span class="lbl b" style="left:14px;top:179px">Question or Comment #1</span>
  <div class="area" style="top:184px;height:17px"></div>
  <span class="lbl b" style="left:14px;top:210px">Question or Comment #2</span>
  <div class="area" style="top:215px;height:17px"></div>
  <span class="lbl b" style="left:14px;top:240px">Question or Comment #3</span>
  <div class="area" style="top:245px;height:17px"></div>
</section>

<section class="pg" style="left:40px;top:367px">
  <div class="brand sm"><span class="dot"></span>HWA</div>
  <h2 class="sh" style="top:27px">CONSENT &amp; SIGNATURE</h2>
  <span class="opt" style="left:41px;top:42px"><b class="cb"></b>&nbsp;&nbsp;HWA Patient Assistance Fund</span><span class="req" style="top:43px">Required</span>
  <span class="opt" style="left:41px;top:52px"><b class="cb"></b>&nbsp;&nbsp;Assignment of Benefits</span><span class="req" style="top:53px">Required</span>
  <span class="opt" style="left:41px;top:62px"><b class="cb"></b>&nbsp;&nbsp;Consent Forms</span><span class="req" style="top:63px">Required</span>
  <span class="opt" style="left:41px;top:71px"><b class="cb"></b>&nbsp;&nbsp;HIPAA Data Use Agreement</span><span class="req" style="top:72px">Required</span>
  <div class="row-line" style="left:40px;right:36px;top:48px"></div>
  <div class="row-line" style="left:40px;right:36px;top:58px"></div>
  <div class="row-line" style="left:40px;right:36px;top:68px"></div>
</section>

<section class="pg" style="left:266px;top:367px">
  <div class="brand lg"><span class="dot"></span>HWA</div>
  <h1 class="title">HWA PATIENT ASSISTANCE FUND</h1>
  <div class="copy" style="top:58px">
    <p>Harbor Wellness Alliance Inc is a free clinic for all that need it. Any patient making less than 250K for a single-member household or under 500k for a multi-member household is eligible to enroll in our patient assistance fund.</p>
    <p style="margin-bottom:0">The patient assistance fund covers</p>
    <ul>
      <li>-Any patient responsibility for medical services including</li>
      <li>-Co-Payments</li>
      <li>-Co-Insurance</li>
      <li>-Deductibles</li>
      <li>-Out of Pocket Cost</li>
      <li>-No Insurance Coverage</li>
    </ul>
    <p>The patient assistance fund DOES NOT cover costs of medications, HOWEVER, HWA works with various patient assistance programs to bring the cost of medications down to little to no cost for our patients.</p>
    <p><strong>If accepted into the patient assistance fund, your insurance may still be billed but Harbor Wellness Alliance Inc will not bill you.</strong></p>
    <p>By signing this document you attest that you meet the income requirements for the HWA Patient Assistance fund. If you choose not to apply, you may be billed for any out of pocket expenses that you may be responsible for.</p>
  </div>
</section>

<section class="pg" style="left:492px;top:367px">
  <div class="brand lg"><span class="dot"></span>HWA</div>
  <h1 class="title">ASSIGNMENT OF BENEFITS AND AUTHORIZATION</h1>
  <div class="copy" style="top:58px">
    <p>While Harbor Wellness Alliance Inc is waiting for payment for all of the fees, I agree to provide the office with information and forms regarding any source of potential payment, to assist in any way I can, and:</p>
    <ol>
      <li>I hereby assign Harbor Wellness Alliance Inc my rights to receive payments from the insurance companies responsible for my claim.</li>
      <li>I also hereby authorize the direct payment to Harbor Wellness Alliance Inc of any sum I now or hereafter owe by any insurance company obligated to make payment to me or you based in whole or in part upon the charges made for your services.</li>
      <li>You are authorized to release any information including the diagnosis and records of any such treatment to any insurance company to process any claims for reimbursement of charges incurred. <strong>THIS IS A DIRECT ASSIGNMENT OF MY RIGHTS AND BENEFITS UNDER THIS POLICY.</strong></li>
    </ol>
    <p><strong>If you have applied for the HWA Patient Assistance fund, you will not be billed for any balances or out of pocket costs.</strong></p>
  </div>
</section>

<section class="pg" style="left:718px;top:367px">
  <div class="brand lg"><span class="dot"></span>HWA</div>
  <h1 class="title">INFORMED CONSENT</h1>
  <div class="copy" style="top:57px">
    <p>I hereby request and consent to the performance of medical services on me (or on the patient named below, for whom I am legally responsible) by the staff or consultants employed or contracted at the Harbor Wellness Alliance Inc. This includes medical services including but not limited to examination, testing, and treatment of various diseases including HIV, sexually transmitted infections, or any diseases conditions that I present for.</p>
    <p>I understand that the results of the tests may have to be reported to the proper government agencies and by signing this agreement I agree to have my information released to any government organization.</p>
    <p>I understand and I am informed that, as is with all healthcare procedures and treatments there are some risks including, but not limited to punctures, abrasions, cuts, infections, misdiagnoses and injuries possibly resulting in death. I do not expect the provider to be able to anticipate and explain all risks and complications, and I wish to rely on the provider to exercise judgment during the course of the procedure with which the provider feels at the time, based upon the facts then known, is in my best interests.</p>
    <p>I also understand that any information not provided to my provider cannot be taken into consideration for my healthcare needs. I understand that with any test, there is a chance for false positives and negatives as well as injury. I will hold harmless the state health department and the Harbor Wellness Alliance Inc, its employees, contractors, and subsidiaries for any damages or injuries that I may suffer as a result of being a patient at the Harbor Wellness Alliance Inc.</p>
    <p>These risks also include psychological or physical harm which can result in permanent disability, emotional loss, death or damage to personal property.</p>
    <p>I understand and have been informed that I have the right to a second opinion and secure other opinions if I have concerns as to the nature of my symptoms and treatment options. I have had the chance to inform the office of any or all previous medical conditions or medications that I may have been diagnosed with or prescribed and that information is accurate to the best of my ability.</p>
    <p>I enter into this agreement freely and understand that its duration will last for as long as I am a patient of the Harbor Wellness Alliance Inc.</p>
    <p>I have read, or have had read to me, the above consent. I am 18 years or older or a representative of a minor/person that has been deemed by the courts to be under my care.</p>
    <p>This document is governed by state law.</p>
    <p style="margin-top:6px">If you are a minor or if you are being represented by another party please provide the appropriate person's:</p>
  </div>
  <div class="sig" style="left:23px">Date</div>
  <div class="sig" style="left:147px">Signature</div>
</section>

<section class="pg" style="left:943px;top:367px">
  <div class="brand lg"><span class="dot"></span>HWA</div>
  <h1 class="title">CONSENT AUTHORIZATION TO USE OR DISCLOSE PROTECTED HEALTH INFORMATION</h1>
  <div class="copy" style="top:65px">
    <p>Your authorization is requested for purposes of delivering your care in an open-door environment as described in the office's privacy notice.</p>
    <p>In the course of your care, in this environment, routine details of your condition and care may be disclosed to other patients or staff in the approximate vicinity of where your care is being delivered. We cannot assure that any of the details of your care will be addressed and considered as confidential by other patients.</p>
    <p>We are requesting your authorization in this regard to assure that you are fully informed and in agreement with the method and circumstances in which we deliver treatment. Your care will not be conditioned on your agreement to this authorization. You have the right not to sign this authorization and you also have the right to revoke this authorization at a later date if that is your wish. If you wish to revoke this authorization at some time in the future please advise us accordingly in writing. You always have the right to review our most updated PHI information. You can also contact our privacy officer at privacy@harborwell.org</p>
    <p>By signing this agreement, you also agree to allow Harbor Wellness Alliance Inc to release any and all of your information to entities it has working relationships with including pharmacies, nursing services, and third-party payers.</p>
    <p>If you agree to this authorization and have received and reviewed our office's HIPAA privacy notice please sign and date below. A copy of this authorization will be maintained by this office.</p>
    <p>Thank you for your cooperation and understanding.</p>
    <p style="margin-top:6px">If you are a minor or if you are being represented by another party please provide the appropriate person's:</p>
  </div>
  <div class="sig" style="left:23px">Date</div>
  <div class="sig" style="left:147px">Signature</div>
</section>

</body>
</html>
```